Business Card Design needed for letterhead design project

This project is linked to Letterhead Design For Corporate.

Our company needs a Business Card Design. Please refer to our original project in the link above.

Industry/Entity Type

Business

```html
<!DOCTYPE html>
<html lang="en">
<head>
<meta charset="utf-8">
<title>Veralis Business Card</title>
<link rel="stylesheet" href="https://fonts.googleapis.com/css2?family=Lato:wght@300;400;700&display=swap">
<style>
  :root {
    --backdrop: #e3e3e3;
    --paper: #ffffff;
    --green: #0d5443;
    --green-light: #0f604c;
    --brand: #2e6a57;
    --mark-tint: #e3ede8;
    --ink-light: #ffffff;
  }
  * { margin: 0; padding: 0; box-sizing: border-box; }
  html, body {
    width: 1026px;
    height: 1200px;
    overflow: hidden;
    background: var(--backdrop);
    font-family: "Lato", sans-serif;
  }
  .canvas { position: relative; width: 1026px; height: 1200px; }

  .card {
    position: absolute;
    width: 958px;
    height: 548px;
    background: var(--paper);
    overflow: hidden;
  }
  .card--front { left: 34px; top: 34px; }
  .card--back { left: 30px; top: 622px; height: 547px; }

  .brand-mark {
    position: absolute;
    border-radius: 50%;
    background: var(--mark-tint);
    transform: translateX(-50%);
  }
  .card--front .brand-mark { left: 170px; top: 14px; width: 160px; height: 160px; }
  .card--back .brand-mark { left: 510px; top: 160px; width: 170px; height: 170px; }

  .brand {
    position: absolute;
    font-family: "Lato", sans-serif;
    font-weight: 700;
    color: var(--brand);
    letter-spacing: 1px;
    line-height: 1;
    white-space: nowrap;
    transform: translateX(-50%);
  }
  .card--front .brand { left: 170px; top: 180px; font-size: 34px; }
  .card--back .brand { left: 510px; top: 344px; font-size: 36px; }

  .name-panel {
    position: absolute;
    left: 586px;
    top: 0;
    width: 372px;
    height: 236px;
    background: var(--green);
    border-bottom-left-radius: 115px;
    color: var(--ink-light);
    text-align: right;
    padding-right: 42px;
    padding-top: 80px;
  }
  .name-panel__name {
    font-weight: 300;
    font-size: 48px;
    line-height: 1;
    letter-spacing: 0.5px;
  }
  .name-panel__role {
    font-weight: 300;
    font-size: 22px;
    line-height: 1.2;
    margin-top: 0;
  }

  .contact-panel {
    position: absolute;
    left: 0;
    top: 244px;
    width: 586px;
    height: 304px;
    background: var(--green);
    border-top-right-radius: 110px;
    color: var(--ink-light);
    padding-left: 52px;
    padding-top: 39px;
  }
  .contact-panel__group { font-size: 26px; line-height: 30px; }
  .contact-panel__group + .contact-panel__group { margin-top: 25px; }
  .contact-panel__phones, .contact-panel__address { font-weight: 300; }
  .contact-panel__web { font-weight: 400; }

  .back-band {
    position: absolute;
    left: 0;
    bottom: 0;
    width: 958px;
    height: 51px;
  }
</style>
</head>
<body>
<div class="canvas">
  <section class="card card--front">
    <div class="brand-mark" aria-hidden="true"></div>
    <div class="brand">VERALIS</div>

    <div class="name-panel">
      <div class="name-panel__name">JOEL BRANT</div>
      <div class="name-panel__role">GRAPHIC WORKER</div>
    </div>

    <div class="contact-panel">
      <div class="contact-panel__group contact-panel__phones">
        02 456 7810 345<br>03 6874 3091
      </div>
      <div class="contact-panel__group contact-panel__web">
        YOUREMAIL@WEBSITE.COM<br>WWW.WEBSITE.COM
      </div>
      <div class="contact-panel__group contact-panel__address">
        48/B HARBOUR LANE, SYDNEY,<br>AUSTRALIA-2000
      </div>
    </div>
  </section>

  <section class="card card--back">
    <div class="brand-mark" aria-hidden="true"></div>
    <div class="brand">VERALIS</div>
    <svg class="back-band" viewBox="0 0 958 51" aria-hidden="true">
      <path d="M522 51 Q550 0 600 0 L958 0 L958 51 Z" fill="var(--green-light)"/>
      <path d="M0 0 L445 0 C495 0 515 15 540 51 L0 51 Z" fill="var(--green)"/>
    </svg>
  </section>
</div>
</body>
</html>
```